Willowmere Cremations Business Cards

To create a business card for my company Willowmere Cremations. Remember it is a cremation company.
We want to make sure people have a business card and information. Something modern, professional
100% Online
Prices starting at $695 all-inclusive (prices subject to change without notice).
A business card is the first point of contact with the prospective client.

Contact Information for Business Card

(305) 472-8163
www.WillowmereCremationsMiami.example
willowmerecremations@mailbox.example

Requirements
Must have
• 100% Online
Prices starting at $695 all-inclusive (prices subject to change without notice)

(305) 472-8163

Must match logo style
Should not have
• No black backgrounds. Please only use the white, orange and blue from the logo

```html
<!DOCTYPE html>
<html lang="en">
<head>
<meta charset="utf-8">
<title>Willowmere Cremations – Business Cards</title>
<link href="https://fonts.googleapis.com/css2?family=Lato:wght@400;700&display=swap" rel="stylesheet">
<style>
  :root {
    --orange: #e8891f;
    --orange-deep: #e4621f;
    --blue: #219ed9;
    --white: #ffffff;
    --frame: #9a9a9a;
    --page: #ffffff;
  }
  html, body {
    margin: 0;
    padding: 0;
    width: 1045px;
    height: 1200px;
    overflow: hidden;
    background: var(--page);
    font-family: "Lato", Arial, sans-serif;
  }
  .sheet {
    position: relative;
    width: 1028px;
    height: 1181px;
    transform: scale(1.0165, 1.0161);
    transform-origin: 0 0;
  }
  .card {
    position: absolute;
    left: 1px;
    width: 1026px;
    box-sizing: border-box;
    border: 1.5px solid var(--frame);
    overflow: hidden;
  }
  .card--front { top: 1px; height: 578px; background: var(--white); }
  .card--back { top: 601px; height: 580px; background: var(--blue); }

  .brand {
    position: absolute;
    text-align: center;
  }
  .brand__disc {
    display: block;
    margin: 0 auto;
    border-radius: 50%;
    background: linear-gradient(135deg, var(--orange) 30%, var(--orange-deep));
  }
  .brand__name {
    display: block;
    font-weight: 700;
    white-space: nowrap;
    letter-spacing: 1px;
  }
  .card--front .brand { left: 0; right: 0; top: 80px; }
  .card--front .brand__disc { width: 210px; height: 210px; }
  .card--front .brand__name { color: var(--blue); font-size: 50px; margin-top: 36px; }

  .card--back .brand { left: 560px; width: 420px; top: 50px; }
  .card--back .brand__disc { width: 180px; height: 180px; }
  .card--back .brand__name { color: var(--white); font-size: 32px; margin-top: 40px; }

  .tab {
    position: absolute;
    top: 470px;
    height: 65px;
    color: var(--white);
    display: flex;
    flex-direction: column;
    justify-content: center;
  }
  .tab--online {
    left: 0;
    width: 264px;
    background: linear-gradient(90deg, var(--orange), var(--orange-deep));
    border-top-right-radius: 16px;
    font-weight: 700;
    font-size: 30px;
    padding-left: 49px;
    box-sizing: border-box;
  }
  .tab--price {
    right: 0;
    width: 467px;
    background: var(--blue);
    border-top-left-radius: 16px;
    text-align: center;
    line-height: 1.15;
  }
  .tab--price .price { font-size: 22px; }
  .tab--price .note { font-size: 18px; }

  .person {
    position: absolute;
    left: 77px;
    top: 293px;
    margin: 0;
    color: var(--white);
    font-weight: 700;
    font-size: 36px;
  }
  .contacts {
    position: absolute;
    left: 76px;
    top: 370px;
    margin: 0;
    padding: 0;
    list-style: none;
    color: var(--white);
    font-size: 28px;
  }
  .contacts li {
    display: flex;
    align-items: center;
    height: 52px;
    white-space: nowrap;
  }
  .contacts svg {
    width: 32px;
    height: 32px;
    margin-right: 27px;
    flex: none;
  }
  .icon-line { fill: none; stroke: var(--orange); stroke-width: 2.5; }
  .icon-fill { fill: var(--orange); }
  .icon-cut { fill: none; stroke: var(--blue); stroke-width: 2; }
</style>
</head>
<body>
<div class="sheet">

  <section class="card card--front">
    <div class="brand">
      <span class="brand__disc"></span>
      <span class="brand__name">Willowmere Cremations</span>
    </div>
    <div class="tab tab--online">100% Online</div>
    <div class="tab tab--price">
      <span class="price">Prices starting at $695 all-inclusive</span>
      <span class="note">(prices subject to change without notice)</span>
    </div>
  </section>

  <section class="card card--back">
    <div class="brand">
      <span class="brand__disc"></span>
      <span class="brand__name">Willowmere Cremations</span>
    </div>
    <h2 class="person">Person Name</h2>
    <ul class="contacts">
      <li>
        <svg viewBox="0 0 32 32" aria-hidden="true">
          <rect class="icon-line" x="7" y="2" width="18" height="28" rx="4" style="stroke-width:3"/>
          <rect class="icon-fill" x="13" y="24" width="6" height="2"/>
        </svg>
        (305) 472-8163
      </li>
      <li>
        <svg viewBox="0 0 32 32" aria-hidden="true">
          <rect class="icon-fill" x="1" y="6" width="30" height="21" rx="2"/>
          <path class="icon-cut" d="M2 8 L16 19 L30 8"/>
          <path class="icon-cut" d="M2 26 L12 16 M30 26 L20 16" style="stroke-width:1.5"/>
        </svg>
        www.WillowmereCremationsMiami.example
      </li>
      <li>
        <svg viewBox="0 0 32 32" aria-hidden="true">
          <g class="icon-line">
            <circle cx="16" cy="16" r="13"/>
            <ellipse cx="16" cy="16" rx="6" ry="13"/>
            <path d="M3 16 H29 M5 9 H27 M5 23 H27"/>
          </g>
        </svg>
        willowmerecremations@mailbox.example
      </li>
    </ul>
  </section>

</div>
</body>
</html>
```